Ecommerce Web Design (E - File Copyright Denver, CO)

This is a service style web design. It is a stand alone website that will eventually be linked to another website (quenvoral.com). But for the time being it is a stand alone website. It will only offer 3-4 products (Services) but have a gallery page with tabs for selling copyrighted material for clients like Pixdune. I will require the following pages:

Only Web Pages, No Coding

Home Page
Products Page
Customer Registration Page
Copyright Information Page (Is being done by a third party for now)
Store for Gallery of all Copyrighted material (with Tabs for Photo, Art, Literature, Manuscripts, Video, etc) to quenvoral.com
Blog Page
About Us Page/Contact US page (all on same page)
User agreement & Privacy Statement Page
Page to look at the borrowers Copyright Files (will be linked to a DB for access via customer unique password and login
FAQ Page

My customers will be Authors, Artist, Photographers, Playwright's, Lawyers, Film rights, software and Corporate Web Designers. We are a third party electronic copyright service offering protection of intellectual property. The site needs to convey Trust, Integrity, Stability, Safety and Strength. I also want to appeal to the artist creativity and want the site to look friendly, hence the logo design. Simple colorful. The site will also have links to social media, Chatterlane, Yonder+, WorkMesh and Chirplo.

Competitor Website:
zantreb.com
http://vellomarkrights.com/
http://tornwisp.quillpage.com/2011/03/pixdune-alternative-image-hosting-and.html

The ecommerce will offer payment from Coinvey, Vessora, TrustPlate and Kavo via tallyforge. The site will also have SSL certificate.

Product 1- Online Copyright Registration
Product 2- Update to Copyright Registration
Product 3- File Copyright to Federal Rights Bureau (Hall of National Records)

The company logo is attached to this file for your preview. I will require additional logos or Icons for all three products (The copy of the Hall Of National Records is also attached for your preview) please feel free to use your own version for the logos/Icons. I'm not a designer and lack artistic impressions as to what I want, but when I see the designs I will know if its the right one.

The website will function as a registration point for Intellectual property copyrights and will also function as a source for infringement searches of the material online. The term "Third Party Electronic Copyright Protection" should be used on the Home Page. Please if you have any questions please ask. I will respond to all entries and correspondence. I work from home and have the ability to respond at a moments notice. That being said I am located in Denver, CO USA, so keep in mind my time zone when you send correspondence to me.
Updates

Good morning or Evening all, There are 10 days left to get your design ideas in. I am very pleased with the results so far. Make sure to email me if you have any questions. Have a great day everyone. Gerald

```html
<!DOCTYPE html>
<html lang="en">
<head>
<meta charset="utf-8">
<title>Rightsafe – Third Party Electronic Copyright Protection</title>
<link href="https://fonts.googleapis.com/css2?family=Montserrat:wght@400;500;600&family=Arimo:ital,wght@0,400;1,400&display=swap" rel="stylesheet">
<style>
:root{
  --green:#8cc63f;
  --green-dark:#74ad2b;
  --ink:#2b2b2b;
  --body:#555;
  --muted:#888;
  --rule:#dcdcdc;
  --header-bg:#f4f4f4;
  --footer-bg:#333333;
  --footer-text:#aaa;
}
*{box-sizing:border-box;margin:0;padding:0}
html,body{width:928px;height:1200px;overflow:hidden;background:#fff}
body{position:relative;font-family:"Arimo",Arial,sans-serif;color:var(--body)}
.abs{position:absolute}
.heading{font-family:"Montserrat",sans-serif;color:var(--ink);font-weight:500;text-transform:uppercase}
.btn{position:absolute;background:var(--green);color:#fff;font-size:8px;display:flex;align-items:center;justify-content:center;text-transform:uppercase;border-radius:2px}
.photo{position:absolute}

/* header */
.site-header{position:absolute;left:0;top:0;width:928px;height:49px;background:var(--header-bg);border-bottom:1px solid var(--rule)}
.brand{position:absolute;left:132px;top:12px;display:flex;align-items:center;gap:6px}
.brand-mark{width:20px;height:20px;background:var(--green)}
.brand-name{font-family:"Montserrat",sans-serif;font-size:17px;font-weight:600;color:var(--green);letter-spacing:1px}
.main-nav{position:absolute;left:290px;top:0;height:48px;display:flex}
.main-nav a{display:flex;align-items:center;padding:0 10px;font-size:7.5px;color:#555;text-decoration:none;border-left:1px solid var(--rule)}
.main-nav a:last-child{border-right:1px solid var(--rule)}
.search{position:absolute;left:660px;top:15px;width:135px;height:20px;border:1px solid var(--rule);background:#fff;font-size:7.5px;color:#999;padding:5px 8px}
.search svg{position:absolute;right:0;top:0;width:20px;height:18px;border-left:1px solid var(--rule)}

/* strapline */
.strap{position:absolute;left:0;top:49px;width:928px;height:48px;border-bottom:1px solid var(--rule)}
.strap h1{position:absolute;left:131px;top:17px;font-size:12.5px}

/* slider */
.slider{left:132px;top:114px;width:427px;height:304px;background:radial-gradient(ellipse at 50% 110%,#4a90d9 0%,#1a3f8f 35%,#0b1b5a 60%,#050c35 100%)}
.slider h2{position:absolute;top:34px;width:100%;text-align:center;font-family:"Montserrat",sans-serif;font-weight:500;color:#fff;font-size:20px;line-height:26px}
.slider p{position:absolute;top:96px;left:30px;right:30px;text-align:center;color:#fff;font-size:9.3px;line-height:18.5px}
.slider-arrows{position:absolute;right:12px;bottom:10px;display:flex;gap:2px}
.slider-arrows span{width:18px;height:18px;background:rgba(255,255,255,.15);display:flex;align-items:center;justify-content:center}

/* recent posts */
.section-title{font-size:11px}
.pager{position:absolute;display:flex;gap:4px}
.post{position:absolute;left:580px;width:215px}
.post .thumb{position:absolute;left:0;top:0;width:82px;height:57px}
.post h4{position:absolute;left:96px;top:0;width:125px;font-weight:400;font-size:7.2px;line-height:14.5px;color:var(--ink);text-transform:uppercase}
.post p{position:absolute;left:96px;top:33px;width:112px;font-size:7.2px;line-height:14.5px;color:var(--body)}
.post-rule{position:absolute;left:580px;width:215px;height:1px;background:var(--rule)}

/* products */
.product h3{position:absolute;font-size:10px;line-height:15.5px}
.product .pic{position:absolute;width:203px;height:110px;border-top:3px solid var(--green)}
.product p{position:absolute;width:205px;font-size:8.5px;line-height:17.3px}

/* services */
.service{position:absolute;top:723px;width:151px;height:106px}
.service span{position:absolute;left:0;bottom:0;width:100%;height:24px;background:rgba(0,0,0,.6);font-family:"Montserrat",sans-serif;color:var(--green);font-size:9.5px;padding:6px 10px}

/* about / testimonial */
.about-text{left:305px;top:889px;width:210px;font-size:8.5px;line-height:17.3px}
.quote{left:561px;top:884px;width:210px;font-size:8.5px;line-height:17.3px;font-style:italic}
.quote-mark{position:absolute;font-family:Georgia,serif;color:#bbb;font-size:18px}
.person-name{left:631px;top:953px;color:var(--green);font-size:9px;font-family:"Montserrat",sans-serif;text-transform:uppercase}
.person-role{left:631px;top:971px;color:var(--ink);font-size:8.5px}

/* partners */
.partner{position:absolute;top:1046px;width:103px;height:70px;border:2px solid #e6e6e6;display:flex;align-items:center;justify-content:center;gap:5px;font-family:"Montserrat",sans-serif;font-weight:600;font-size:12px;color:#1d3f8f}

/* footer */
.site-footer{position:absolute;left:0;top:1136px;width:928px;height:64px;background:var(--footer-bg)}
.site-footer .brand{left:134px;top:20px}
.site-footer .brand-mark{background:#666}
.site-footer .brand-name{color:#777}
.foot-nav{position:absolute;left:288px;top:18px;display:flex;gap:18px;font-size:6.5px;color:var(--footer-text);text-transform:uppercase}
.foot-copy{position:absolute;left:288px;top:38px;font-size:6.3px;color:var(--footer-text)}
.social{position:absolute;left:660px;top:24px;display:flex;gap:10px}
.social span{display:flex;align-items:center;gap:4px;font-size:7.5px;color:#ccc}
.social i{width:9px;height:9px;border:1px solid #999;border-radius:50%}
</style>
</head>
<body>

<header class="site-header">
  <div class="brand"><div class="brand-mark"></div><div class="brand-name">RIGHTSAFE</div></div>
  <nav class="main-nav">
    <a>HOME</a><a>ABOUT US</a><a>PRODUCTS</a><a>SERVICES</a><a>REGISTRATION</a><a>CONTACT US</a>
  </nav>
  <div class="search">Search :
    <svg viewBox="0 0 20 18"><circle cx="9.5" cy="8.5" r="3" fill="none" stroke="#aaa" stroke-width="1"/><line x1="11.7" y1="10.7" x2="14" y2="13" stroke="#aaa"/></svg>
  </div>
</header>

<section class="strap">
  <h1 class="heading">Rightsafe protect your copyrights, online and for free!</h1>
  <div class="btn" style="left:634px;top:10px;width:161px;height:28px">Click here for joined now</div>
</section>

<div class="photo slider" role="img" aria-label="Earth seen from space at night with a glowing blue horizon">
  <h2>THIRD PARTY ELECTRONIC<br>COPYRIGHT PROTECTION</h2>
  <p>We are a third party electronic copyright service offering protection of intellectual property. Our customers will be Authors, Artist, Photographers, Playwright's, Lawyers, Film rights, software and Corporate Web Designers.</p>
  <div class="slider-arrows">
    <span><svg width="6" height="8"><path d="M5 0L1 4l4 4" fill="none" stroke="#ccc"/></svg></span>
    <span><svg width="6" height="8"><path d="M1 0l4 4-4 4" fill="none" stroke="#ccc"/></svg></span>
  </div>
</div>

<h3 class="heading section-title abs" style="left:579px;top:114px">Recent posts</h3>
<div class="pager" style="left:777px;top:117px"><svg width="14" height="8"><path d="M4 1L1 4l3 3M10 1l3 3-3 3" fill="none" stroke="#888"/></svg></div>
<div class="post-rule" style="top:139px;height:2px;background:#bbb"></div>

<article class="post" style="top:155px">
  <div class="thumb photo" role="img" aria-label="Hand holding a globe mesh" style="background:linear-gradient(135deg,#9fc4e6,#3d6aa0)"></div>
  <h4>Lorem ipsum is simply dummy text of the printing</h4>
  <p>Lorem Ipsum is simply dummy text of the printing...</p>
</article>
<div class="post-rule" style="top:226px"></div>
<article class="post" style="top:238px">
  <div class="thumb photo" role="img" aria-label="Blue arrow breaking through a wall" style="background:linear-gradient(135deg,#f0f0f0,#cfd8e2)"></div>
  <h4>Lorem ipsum is simply dummy text of the printing</h4>
  <p>Lorem Ipsum is simply dummy text of the printing...</p>
</article>
<div class="post-rule" style="top:309px"></div>
<article class="post" style="top:324px">
  <div class="thumb photo" role="img" aria-label="Computer mouse on a dark desk" style="background:linear-gradient(135deg,#3b3f45,#7a7f86)"></div>
  <h4>Lorem ipsum is simply dummy text of the printing</h4>
  <p>Lorem Ipsum is simply dummy text of the printing...</p>
</article>
<div class="btn" style="left:580px;top:395px;width:90px;height:22px">View more</div>

<div class="product">
  <h3 class="heading abs" style="left:134px;top:447px">Online copyright<br>registration</h3>
  <div class="pic photo" role="img" aria-label="Hands typing on a laptop keyboard" style="left:132px;top:487px;background:linear-gradient(160deg,#e8edf2,#8c9bab 60%,#3b4552)"></div>
  <p class="abs" style="left:132px;top:606px">Lorem Ipsum is simply dummy text of the printing and typesetting industry. Lorem Ipsum has been the industry's standard dummy...</p>
</div>
<div class="product">
  <h3 class="heading abs" style="left:366px;top:447px">Update to copyright<br>registration</h3>
  <div class="pic photo" role="img" aria-label="Two hands around a glowing glass sphere on blue" style="left:364px;top:487px;background:radial-gradient(circle at 50% 50%,#e8f2ff 0%,#5fa0e6 30%,#1b56b8 70%,#0f3a8a)"></div>
  <p class="abs" style="left:364px;top:606px">Lorem Ipsum is simply dummy text of the printing and typesetting industry. Lorem Ipsum has been the industry's standard dummy...</p>
</div>
<div class="product">
  <h3 class="heading abs" style="left:594px;top:447px">File copyright to us<br>copyright office</h3>
  <div class="pic photo" role="img" aria-label="Business people walking down a bright blue corridor" style="left:592px;top:487px;background:radial-gradient(ellipse at 40% 55%,#f4f9ff 0%,#9ccaf0 40%,#3f7fc4 100%)"></div>
  <p class="abs" style="left:592px;top:606px">Lorem Ipsum is simply dummy text of the printing and typesetting industry. Lorem Ipsum has been the industry's standard dummy...</p>
</div>

<h3 class="heading section-title abs" style="left:132px;top:690px">Managing your copyrights with Rightsafe is this easy:</h3>
<div class="pager" style="left:779px;top:693px"><svg width="14" height="8"><path d="M4 1L1 4l3 3M10 1l3 3-3 3" fill="none" stroke="#888"/></svg></div>
<div class="service photo" role="img" aria-label="Woman with a bicycle in a golden field" style="left:132px;background:linear-gradient(160deg,#b8a26a,#6d5b30)"><span>SERVICES - 01</span></div>
<div class="service photo" role="img" aria-label="Law books and a judge's gavel" style="left:303px;background:linear-gradient(160deg,#5a4a2c,#231a0f)"><span>SERVICES - 02</span></div>
<div class="service photo" role="img" aria-label="Smiling photographer with camera and city lights" style="left:474px;background:linear-gradient(160deg,#c8822a,#6a2a18)"><span>SERVICES - 03</span></div>
<div class="service photo" role="img" aria-label="Rock arch over the sea at sunset" style="left:644px;background:linear-gradient(170deg,#f0a24a,#b35a20 55%,#4a2a18)"><span>SERVICES - 04</span></div>

<h3 class="heading section-title abs" style="left:134px;top:860px">About Rightsafe</h3>
<div class="photo" role="img" aria-label="Business handshake in front of city towers" style="left:132px;top:889px;width:153px;height:118px;background:linear-gradient(160deg,#2f5fa8,#9fc0e0 60%,#e8eef5)"></div>
<p class="abs about-text">Lorem Ipsum is simply dummy text of the printing and typesetting industry. Lorem Ipsum has been the industry's standard dummy Lorem Ipsum is simply dummy text of the printing and typesetting industry. Lorem Ipsum has been the industry's...</p>
<div class="btn" style="left:305px;top:985px;width:90px;height:22px">Read more</div>

<h3 class="heading section-title abs" style="left:539px;top:860px">Testimonials</h3>
<div class="pager" style="left:779px;top:863px"><svg width="14" height="8"><path d="M4 1L1 4l3 3M10 1l3 3-3 3" fill="none" stroke="#888"/></svg></div>
<span class="quote-mark" style="left:540px;top:880px">&ldquo;</span>
<p class="abs quote">Lorem Ipsum is simply dummy text of the printing and typesetting industry. Lorem Ipsum has been the industry's standard dummy...</p>
<span class="quote-mark" style="left:774px;top:918px">&rdquo;</span>
<div class="photo" role="img" aria-label="Portrait of the client reviewer" style="left:558px;top:954px;width:58px;height:51px;border:2px solid #e6e6e6;background:linear-gradient(160deg,#e4e8ec,#b8c2cc)"></div>
<div class="abs person-name">Marcel Tovin</div>
<div class="abs person-role">Marketing executive</div>

<div class="partner" style="left:132px"><svg width="56" height="56"><circle cx="28" cy="28" r="24" fill="none" stroke="#c9302c" stroke-width="3"/></svg></div>
<div class="partner" style="left:244px"><svg width="40" height="40"><rect x="4" y="4" width="32" height="32" fill="#1d4f9c"/></svg></div>
<div class="partner" style="left:356px"><svg width="56" height="56"><circle cx="28" cy="28" r="24" fill="none" stroke="#7a8a99" stroke-width="3"/></svg></div>
<div class="partner" style="left:469px">Vessora</div>
<div class="partner" style="left:580px;color:#c9302c">TrustPlate</div>
<div class="partner" style="left:692px;color:#2a7ac0">Cardlume</div>

<footer class="site-footer">
  <div class="brand"><div class="brand-mark"></div><div class="brand-name">RIGHTSAFE</div></div>
  <nav class="foot-nav"><span>Home</span><span>About us</span><span>Products</span><span>Services</span><span>Registration</span><span>Contact us</span></nav>
  <div class="foot-copy">© 2014 RIGHTSAFE. ALL RIGHTS RESERVED</div>
  <div class="social">
    <span><i></i>Chatterlane</span><span><i></i>Chirplo</span><span><i></i>Yonder+</span><span><i></i>WorkMesh</span>
  </div>
</footer>

</body>
</html>
```